We need a small, simple graphic for the company newsletter. The topic of this issue is voting. As a company, we believe it is important to vote; therefore, we're going to explain the importance of voting, how to vote, when to vote, and how the company will be providing time off to vote. We would like the graphic to be simple (2-3 colors) and look like the sticker or pin you received after voting that says "I voted". We would like our company logo incorporated somehow, so be creative. It must contain our company color of blue (r 38, g 58, b 128). The company logo is attached, as well as some I voted stickers for reference

Requirements
Must have
• Use our company color of blue (r 38 g 58 b 128). Use the words "I Voted". Use the company font Bebas and/or Helvetica Neue. The background must be white as it will be incorporated into a newsletter document.
Nice to have
• Incorporate the company logo. American flag
Should not have
• fireworks, reference to 2020

```html
<!DOCTYPE html>
<html lang="en">
<head>
<meta charset="utf-8">
<title>I Voted Sticker</title>
<link rel="stylesheet" href="https://fonts.googleapis.com/css2?family=Bebas+Neue&display=swap">
<style>
  :root {
    --brand-blue: #263a80;
    --flag-red: #e0262f;
    --ring-grey: #a7a9ac;
    --paper: #ffffff;
  }
  html, body {
    margin: 0;
    padding: 0;
    width: 1200px;
    height: 1142px;
    overflow: hidden;
    background: var(--paper);
  }
  .canvas {
    width: 1200px;
    height: 1142px;
    position: relative;
  }
  .sticker {
    position: absolute;
    left: 358px;
    top: 330px;
    width: 464px;
    height: 464px;
  }
  .sticker-base { fill: var(--paper); }
  .ring-outer { fill: none; stroke: var(--flag-red); stroke-width: 10; }
  .ring-inner { fill: none; stroke: var(--ring-grey); stroke-width: 4; }
  .flag-field { fill: var(--brand-blue); }
  .flag-star { fill: var(--paper); }
  .flag-stripe { fill: var(--flag-red); }
  .company-name {
    font-family: "Bebas Neue", "Helvetica Neue", Arial, sans-serif;
    font-size: 52px;
    fill: var(--brand-blue);
    letter-spacing: 2px;
  }
  .voted-label {
    font-family: "Bebas Neue", "Helvetica Neue", Arial, sans-serif;
    font-size: 76px;
    fill: var(--brand-blue);
  }
</style>
</head>
<body>
<main class="canvas">
  <svg class="sticker" viewBox="-232 -232 464 464" role="group" aria-label="I Voted sticker">
    <defs>
      <clipPath id="inner-disc">
        <circle r="194"/>
      </clipPath>
      <polygon id="star" points="0,-1 0.2245,-0.309 0.951,-0.309 0.363,0.118 0.588,0.809 0,0.382 -0.588,0.809 -0.363,0.118 -0.951,-0.309 -0.2245,-0.309"/>
    </defs>

    <circle class="sticker-base" r="230"/>
    <circle class="ring-outer" r="211"/>
    <circle class="ring-inner" r="196"/>

    <g clip-path="url(#inner-disc)">
      <rect class="flag-field" x="-200" y="-200" width="400" height="115"/>
      <rect class="flag-stripe" x="-140" y="114" width="280" height="19"/>
      <rect class="flag-stripe" x="-200" y="154" width="400" height="19"/>
    </g>

    <use href="#star" class="flag-star" transform="translate(-70 -127) scale(21)"/>
    <use href="#star" class="flag-star" transform="translate(0 -131) scale(34)"/>
    <use href="#star" class="flag-star" transform="translate(70 -127) scale(21)"/>

    <text class="company-name" x="0" y="6" text-anchor="middle">Kestrel Works</text>
    <text class="voted-label" x="0" y="103" text-anchor="middle">I Voted!</text>
  </svg>
</main>
</body>
</html>
```